The Kestrel Personal Training Studio Information Card

The front and back of card to give people that walk in to our gym. There are a few things to say on the card. But it also needs to be designed in an attractive way. You can make some of the information bullett points or with icons or graphics. Please look at our website at https://thekestrelfitness-example.com/ . The card will be 4" x 9"

Target Market(s)

High End Clientele who want to train in a private gym

Industry/Entity Type

Fitness

Font styles to use
Serif
Sans Serif
Other font styles liked:
• the same font Vorlex uses on the zuntab

Colors
F0912C
F2A743
F7CA91
FBE8D2
FDF5EE

Requirements
Must have
• A cool look

```html
<!DOCTYPE html>
<html lang="en">
<head>
<meta charset="utf-8">
<title>The Kestrel Private Training Studio – Information Card</title>
<link href="https://fonts.googleapis.com/css2?family=Oswald:wght@500;600;700&family=Arimo:ital,wght@0,400;0,700;1,400;1,700&display=swap" rel="stylesheet">
<style>
  :root {
    --red: #e8323c;
    --black: #0a0a0a;
    --charcoal: #2b2b2b;
    --grey: #555a60;
    --text: #333333;
    --white: #ffffff;
    --backdrop: #5f6470;
    --photo-front-a: #4a4d55;
    --photo-front-b: #7b7f88;
    --photo-back-a: #c9d6e3;
    --photo-back-b: #8fa4bd;
  }
  * { margin: 0; padding: 0; box-sizing: border-box; }
  html, body { width: 1200px; height: 1200px; overflow: hidden; }
  body {
    background: var(--backdrop);
    font-family: "Arimo", Arial, sans-serif;
    position: relative;
  }
  .card {
    position: absolute;
    top: 195px;
    width: 360px;
    height: 809px;
    background: var(--white);
    overflow: hidden;
  }
  .card--front { left: 214px; }
  .card--back { left: 641px; }
  .card__art { position: absolute; left: 0; top: 0; width: 360px; height: 310px; }
  .centered { position: absolute; left: 0; width: 100%; text-align: center; }
  .display { font-family: "Oswald", Impact, sans-serif; font-weight: 700; text-transform: uppercase; letter-spacing: 0; }

  /* front */
  .brand { top: 300px; }
  .brand__name {
    font-family: "Oswald", Impact, sans-serif;
    font-weight: 600;
    font-size: 44px;
    line-height: 50px;
    color: var(--grey);
    text-transform: uppercase;
  }
  .brand__name::before {
    content: "";
    display: inline-block;
    width: 14px; height: 14px;
    background: var(--red);
    margin-right: 10px;
    vertical-align: 6px;
  }
  .brand__tagline {
    font-family: "Oswald", sans-serif;
    font-weight: 600;
    font-size: 12px;
    letter-spacing: 4.6px;
    color: var(--grey);
    margin-top: 6px;
  }
  .headline { top: 410px; font-size: 31px; line-height: 31px; }
  .headline__red { color: var(--red); }
  .headline__black { color: var(--black); }
  .start {
    top: 555px;
    left: 35px; width: 290px;
    display: flex; align-items: center; gap: 4px;
    color: var(--red);
    font-weight: 700; font-style: italic; font-size: 17px;
  }
  .start::before, .start::after { content: ""; flex: 1; height: 1.5px; background: var(--red); }
  .start__text { white-space: nowrap; }
  .intro { top: 580px; left: 24px; width: 312px; font-size: 11.2px; line-height: 15px; color: var(--text); }
  .phone { top: 688px; font-weight: 700; font-size: 31px; line-height: 34px; color: var(--red); }
  .email { top: 724px; font-style: italic; font-size: 12.5px; color: var(--text); }
  .web {
    position: absolute; top: 745px; left: 58px; width: 244px; height: 22px;
    background: var(--red); color: var(--white);
    font-weight: 700; font-size: 11.5px; line-height: 22px; text-align: center;
    clip-path: polygon(10px 0, calc(100% - 10px) 0, 100% 50%, calc(100% - 10px) 100%, 10px 100%, 0 50%);
  }
  .address { top: 772px; font-size: 12.5px; color: var(--text); }
  .foot { position: absolute; left: 0; bottom: 0; width: 360px; height: 9px; }

  /* back */
  .approach { top: 302px; }
  .approach__top { font-size: 28px; line-height: 32px; color: var(--red); }
  .approach__bottom { font-size: 19.5px; line-height: 22px; color: var(--black); }
  .about { left: 26px; width: 308px; font-size: 10.4px; line-height: 13.4px; color: var(--text); }
  .about--goals { top: 370px; }
  .about--safety { top: 432px; }
  .rates { position: absolute; top: 522px; left: 35px; width: 294px; }
  .rates__title {
    background: var(--red); color: var(--white);
    height: 36px; line-height: 36px; text-align: center;
    font-family: "Oswald", sans-serif; font-weight: 700; font-size: 23px;
  }
  .rates__row {
    height: 30px; line-height: 30px; text-align: center; color: var(--white);
    font-family: "Oswald", sans-serif; font-weight: 600; font-size: 17px; text-transform: uppercase;
  }
  .rates__row:nth-child(odd) { background: var(--black); }
  .rates__row:nth-child(even) { background: var(--charcoal); }
  .example { position: absolute; top: 722px; left: 37px; width: 180px; color: var(--text); font-size: 11.5px; line-height: 13.5px; }
  .example__label { color: var(--red); font-weight: 700; font-size: 16px; line-height: 18px; }
  .price { position: absolute; top: 718px; right: 33px; text-align: center; }
  .price__amount { font-family: "Oswald", sans-serif; font-weight: 700; font-size: 50px; line-height: 52px; color: var(--red); }
  .price__unit { font-weight: 700; font-size: 11.5px; color: var(--black); }
</style>
</head>
<body>

<section class="card card--front" aria-label="Card front">
  <svg class="card__art" viewBox="0 0 360 310" aria-hidden="false">
    <defs>
      <linearGradient id="frontPhoto" x1="0" y1="0" x2="1" y2="1">
        <stop offset="0" stop-color="var(--photo-front-a)"/>
        <stop offset="1" stop-color="var(--photo-front-b)"/>
      </linearGradient>
    </defs>
    <polygon points="0,0 360,0 360,236 180,292 0,236" fill="url(#frontPhoto)" role="img" aria-label="Photo: a trainer spotting a client doing a barbell squat in a private gym"/>
    <polygon points="0,237 180,275 360,237 360,249 180,288 0,249" fill="var(--red)"/>
    <polygon points="0,253 180,292 360,253 360,257 180,297 0,257" fill="var(--grey)"/>
  </svg>

  <div class="centered brand">
    <div class="brand__name">The Kestrel</div>
    <div class="brand__tagline">PRIVATE TRAINING STUDIO</div>
  </div>

  <h1 class="centered display headline">
    <span class="headline__red">Personal Training<br>at a Private Gym</span><br>
    <span class="headline__black">For Real People Who<br>Want Real Results</span>
  </h1>

  <div class="start"><span class="start__text">How do you get started?</span></div>
  <p class="centered intro">We schedule prospective clients for a no cost or obligation consultation. At that consultation we will do a movement screen with you. This will allow the trainer to see what level of flexibility and strength you are currently at. You will be able to discuss your goals and other issues (injuries, etc) at that time.</p>

  <div class="centered phone">555.010.4477</div>
  <div class="centered email">contact@thekestrelfitness-example.com</div>
  <div class="web">THEKESTRELFITNESS-EXAMPLE.COM</div>
  <div class="centered address">208 Linden Avenue, Millbrook, NC</div>

  <svg class="foot" viewBox="0 0 360 9" aria-hidden="true">
    <polygon points="0,0 260,0 255,9 0,9" fill="var(--black)"/>
    <polygon points="264,0 360,0 360,9 259,9" fill="var(--red)"/>
  </svg>
</section>

<section class="card card--back" aria-label="Card back">
  <svg class="card__art" viewBox="0 0 360 310" aria-hidden="false">
    <defs>
      <linearGradient id="backPhoto" x1="0" y1="0" x2="1" y2="1">
        <stop offset="0" stop-color="var(--photo-back-a)"/>
        <stop offset="1" stop-color="var(--photo-back-b)"/>
      </linearGradient>
    </defs>
    <rect x="0" y="0" width="360" height="280" fill="url(#backPhoto)" role="img" aria-label="Photo: a trainer helping a smiling older man stretch a resistance band overhead"/>
    <polygon points="0,290 180,245 360,290 360,310 0,310" fill="var(--white)"/>
    <polyline points="0,290 180,245 360,290" fill="none" stroke="var(--grey)" stroke-width="4"/>
    <polygon points="0,302 180,256 360,302 360,313 180,266 0,313" fill="var(--red)"/>
  </svg>

  <h2 class="centered display approach">
    <div class="approach__top">A Safe &amp; Individualized</div>
    <div class="approach__bottom">Approach to Strength Training</div>
  </h2>

  <p class="centered about about--goals">Our clients have different goals: Build strength, Increase Flexibility, Improve functional and daily movements, Train for an event, or Weight Loss. We will tailor your training program to the specific results you are looking for.</p>
  <p class="centered about about--safety">Some ways of training increase the chance of injury, we do not practice those types of training at The Kestrel. Many of our clients have current or past injuries that can cause problems. We work with them to not aggravate those injuries or allow them to become an obstacle to their workouts.</p>

  <div class="rates">
    <div class="rates__title">OUR RATES</div>
    <div class="rates__rows">
      <div class="rates__row">All sessions are 60 minutes</div>
      <div class="rates__row">1 time per week: &nbsp;$110 per session</div>
      <div class="rates__row">2 times per week: $85 per session</div>
      <div class="rates__row">3 times per week $80 per session</div>
      <div class="rates__row">Add $40 for a partnered session</div>
    </div>
  </div>

  <div class="example">
    <div class="example__label">Example</div>
    A Partnered Session<br>(2 people training together)<br>coming twice a week is
  </div>
  <div class="price">
    <div class="price__amount">$125</div>
    <div class="price__unit">PER SESSION</div>
  </div>

  <svg class="foot" viewBox="0 0 360 9" aria-hidden="true">
    <polygon points="0,0 260,0 255,9 0,9" fill="var(--red)"/>
    <polygon points="264,0 360,0 360,9 259,9" fill="var(--black)"/>
  </svg>
</section>

</body>
</html>
```